Training Company Needs a Web Design

We are a Training company that needs a website design completed for us. "The Harbor Loft" The website will be a 'community space' specialising in 'Change and Transformation'. It will be a 'space' where individuals can come to find out 'latest news', upcoming events and courses, chat with others and find 'tools and templates'. They will need to login as a 'Member'.

The final design needs to be professional but have a 'fun and interactive' feel and appeal to our target audience who are predominantly corporate individuals.

Target Market(s)

Corporate Individuals - they may have a Change or Project background

Industry/Entity Type

Business Consultant

Number of Pages Required

3 page

Font styles to use
Sans Serif

Requirements
Must have
• Design for 'Home Page'
• A professional and corporate 'feel' but be fun and interactive.
Nice to have
• A 'sense' of how some of the other pages may be designed or laid out.

```html
<!DOCTYPE html>
<html lang="en">
<head>
<meta charset="utf-8">
<title>The Harbor Loft — Home</title>
<link href="https://fonts.googleapis.com/css2?family=Archivo+Black&family=Open+Sans:wght@400;600;700&display=swap" rel="stylesheet">
<style>
:root{
  --orange:#f05a28;
  --yellow:#f2cf3b;
  --teal:#4bd9c0;
  --blue:#0da0dc;
  --navy:#0f4c8c;
  --purple:#8e6fae;
  --ink:#333a40;
  --grey:#777d83;
  --line:#dcdfe2;
  --logo:#1d3f6e;
  --white:#ffffff;
}
*{box-sizing:border-box;margin:0;padding:0}
html,body{width:1200px;height:2675px;overflow:hidden}
body{font-family:"Open Sans",Arial,sans-serif;color:var(--ink);background:var(--white);position:relative}
.band{position:absolute;left:0;width:1200px}
.display{font-family:"Archivo Black","Arial Black",sans-serif;text-transform:uppercase}
.section-title{position:absolute;left:53px;color:var(--white);font-size:24px;font-family:"Archivo Black","Arial Black",sans-serif;letter-spacing:1px}

/* header */
.site-header{top:0;height:184px;background:var(--white)}
.brand{position:absolute;left:53px;top:40px;color:var(--logo);font-weight:600;font-size:37px;line-height:38px;display:flex;align-items:center;gap:16px}
.brand-mark{width:26px;height:26px;background:var(--teal);flex:none}
.contact-line{position:absolute;left:556px;top:44px;display:flex;gap:26px;font-size:15px;color:var(--grey);align-items:center}
.contact-line span{display:flex;align-items:center;gap:8px}
.account{position:absolute;top:39px;height:38px;border:1.5px solid var(--orange);display:flex;align-items:center;gap:10px;font-size:12px;color:var(--blue);padding-right:10px}
.account i{width:32px;height:35px;background:var(--blue);display:flex;align-items:center;justify-content:center}
.member{left:945px;width:102px}
.login{left:1065px;width:89px}
.main-nav{position:absolute;left:458px;top:103px;display:flex;height:67px}
.main-nav a{display:flex;align-items:center;justify-content:center;font-size:16px;color:var(--ink);text-decoration:none;border:1px solid #eceef0;border-top:4px solid;text-transform:uppercase}
.main-nav .active{background:var(--orange);color:var(--white);border-top-color:var(--orange);border-color:var(--orange)}

/* hero */
.hero{top:184px;height:494px;background:var(--orange)}
.hero-photo{position:absolute;left:749px;top:0;width:383px;height:494px;background:linear-gradient(180deg,#e9a37f 0%,#c8b3a6 35%,#6c6a70 70%,#4b4b52 100%);border-radius:190px 190px 0 0;z-index:1}
.hero h1{position:absolute;left:53px;top:98px;color:var(--white);font-size:39px;line-height:59px;font-weight:400;letter-spacing:.5px;white-space:nowrap;z-index:2}
.hero p{position:absolute;left:53px;top:288px;color:var(--white);font-size:19px;font-weight:600;z-index:2}
.btn-register{position:absolute;left:53px;top:347px;width:131px;height:46px;background:#3ed3be;color:var(--white);font-size:19px;display:flex;align-items:center;justify-content:center;z-index:2}

/* about */
.about{top:678px;height:449px;background:var(--yellow)}
.about .section-title{top:44px}
.about-text{position:absolute;left:53px;top:88px;width:1100px;color:var(--white);font-size:16px;line-height:25px}
.features{position:absolute;left:53px;top:165px;width:1100px;display:flex}
.feature{width:282px;text-align:center;color:var(--white)}
.feature-icon{width:110px;height:110px;margin:0 auto;position:relative}
.feature-icon .card{position:absolute;inset:6px;background:var(--white)}
.feature-icon .card.tilt{transform:rotate(8deg);opacity:.9}
.feature-icon svg{position:absolute;inset:0;margin:auto}
.feature h3{margin-top:38px;font-size:17px;font-family:"Archivo Black","Arial Black",sans-serif;font-weight:400;letter-spacing:1px}
.feature p{margin:10px auto 0;width:235px;font-size:13.5px;line-height:21px}

/* courses */
.courses{top:1127px;height:510px;background:var(--teal)}
.courses .section-title{top:44px}
.course-grid{position:absolute;left:53px;top:107px;display:flex;gap:29px}
.course-card{width:253px;height:353px;background:var(--white);padding:9px;box-shadow:0 2px 6px rgba(0,0,0,.15)}
.course-photo{height:198px}
.course-card h3{margin:14px 0 0 2px;font-size:17px;font-weight:700;color:var(--ink)}
.course-card h3.highlight{color:var(--blue)}
.course-card p{margin:4px 0 0 2px;font-size:13.5px;line-height:21px;color:var(--grey)}
.course-meta{display:flex;margin-top:16px;border-top:1px solid var(--line);height:42px;font-size:13px;align-items:center}
.stars{flex:1;color:#6a6f74;letter-spacing:1px;font-size:14px}
.price{border-left:1px solid var(--line);border-right:1px solid var(--line);padding:0 12px;height:100%;display:flex;align-items:center;gap:4px;color:var(--blue)}
.price s{color:var(--ink)}
.seats{padding-left:8px;color:var(--blue);display:flex;align-items:center;gap:3px}

/* news */
.news{top:1637px;height:560px;background:var(--blue)}
.news .section-title{top:44px}
.news-grid{position:absolute;left:53px;top:96px;display:grid;grid-template-columns:535px 537px;gap:28px 29px}
.news-card{height:192px;background:var(--white);display:flex;padding:3px}
.news-photo{width:228px;height:186px;flex:none}
.news-body{padding:14px 0 0 18px}
.news-body h3{font-size:18px;font-weight:600;color:#5a6066}
.news-body h3.highlight{color:var(--blue)}
.news-body p{margin-top:9px;font-size:14.5px;line-height:27px;color:#8a8f94;width:280px}
.btn-more{margin-top:8px;width:118px;height:36px;border:1px solid #bfc3c7;font-size:12px;display:flex;align-items:center;justify-content:center;color:#555}

/* events */
.events{top:2197px;height:383px;background:var(--navy)}
.events .section-title{top:46px}
.event-grid{position:absolute;left:53px;top:94px;display:flex;gap:29px}
.event{width:348px;color:var(--white)}
.event-photo{height:161px}
.event-info{display:flex;gap:14px;margin-top:10px}
.date{width:52px;height:68px;border:1.5px solid var(--white);flex:none;text-align:center;background:var(--navy)}
.date b{display:block;font-size:21px;font-weight:600;height:40px;line-height:40px}
.date span{display:block;background:var(--white);color:var(--ink);font-size:13px;height:25px;line-height:25px}
.event-info p{font-size:16px;line-height:27px;margin-top:2px}

/* footer */
.site-footer{top:2580px;height:95px;background:var(--purple)}
.footer-nav{position:absolute;left:53px;top:21px;font-size:13.5px;color:var(--white);display:flex;gap:14px}
.footer-nav i{font-style:normal;opacity:.8}
.copyright{position:absolute;left:53px;top:54px;font-size:13.5px;color:var(--white)}
.social{position:absolute;left:937px;top:32px;display:flex;gap:22px;align-items:center}
.social span{width:20px;height:20px;border-radius:50%;background:rgba(255,255,255,.85)}
.social span:first-child{width:32px;height:32px}
</style>
</head>
<body>

<header class="band site-header">
  <div class="brand"><span class="brand-mark"></span><span>THE<br>HARBOR<br>LOFT</span></div>
  <div class="contact-line">
    <span><svg width="16" height="16" viewBox="0 0 24 24"><path fill="#0da0dc" d="M6.6 10.8a15 15 0 0 0 6.6 6.6l2.2-2.2a1 1 0 0 1 1-.25 11.4 11.4 0 0 0 3.6.57 1 1 0 0 1 1 1V20a1 1 0 0 1-1 1A17 17 0 0 1 3 4a1 1 0 0 1 1-1h3.5a1 1 0 0 1 1 1c0 1.25.2 2.45.57 3.57a1 1 0 0 1-.25 1z"/></svg>123-456-7890</span>
    <span><svg width="18" height="14" viewBox="0 0 18 14"><rect width="18" height="14" rx="1" fill="#0da0dc"/><path d="M1 1l8 6 8-6" stroke="#fff" stroke-width="1.5" fill="none"/></svg>hello@harborloft.example</span>
  </div>
  <div class="account member"><i><svg width="16" height="18" viewBox="0 0 16 18"><circle cx="8" cy="5" r="4" fill="#fff"/><path d="M0 18a8 7 0 0 1 16 0z" fill="#fff"/></svg></i>MEMBER</div>
  <div class="account login"><i><svg width="18" height="18" viewBox="0 0 18 18"><path d="M7 2h9v14H7" stroke="#fff" stroke-width="2" fill="none"/><path d="M1 9h9M7 5l4 4-4 4" stroke="#fff" stroke-width="2" fill="none"/></svg></i>LOGIN</div>
  <nav class="main-nav">
    <a class="active" style="width:86px">Home</a>
    <a style="width:93px;border-top-color:var(--yellow)">About</a>
    <a style="width:95px;border-top-color:var(--teal)">Course</a>
    <a style="width:137px;border-top-color:var(--blue)">Latest News</a>
    <a style="width:150px;border-top-color:var(--navy)">Latest Events</a>
    <a style="width:137px;border-top-color:var(--purple)">Contact Us</a>
  </nav>
</header>

<section class="band hero">
  <div class="hero-photo" role="img" aria-label="Photo of a smiling businesswoman in a grey suit with arms crossed"></div>
  <h1 class="display">The Harbor Loft<br>The Best Training Company<br>We Prvides Best Services</h1>
  <p>Lorem ipsum dolor sit amet consectetur adipiscing elitorbi facilisisis nisl.</p>
  <div class="btn-register">REGISTER</div>
</section>

<section class="band about">
  <h2 class="section-title">ABOUT</h2>
  <p class="about-text">Lorem ipsum dolor sit amet, consectetur adipiscing elit. Donec hendrerit, tortor non vehicula laoreet, felis tortor congue est, quis feugiat quam velit non tortor. Vivamus a tempus nulla. Suspendisse eu suscipit est, vel viverra turpis. Vivamus malesuada eros odio, ut ullamcor</p>
  <div class="features">
    <div class="feature">
      <div class="feature-icon"><div class="card"></div>
        <svg width="60" height="60" viewBox="0 0 60 60" fill="none" stroke="#4a4f55" stroke-width="2.5"><rect x="6" y="8" width="34" height="26"/><path d="M12 26l8-8 6 5 8-9M23 34v14M14 50l9-16 9 16"/><circle cx="48" cy="20" r="4" fill="#4a4f55"/><path d="M48 26v18M40 30h16"/></svg></div>
      <h3>WE COACH EASY</h3>
      <p>Doloremque laudantium, totam rem aperiam, eaque ipsa quae ab illo inventore</p>
    </div>
    <div class="feature">
      <div class="feature-icon"><div class="card tilt"></div><div class="card"></div>
        <svg width="60" height="60" viewBox="0 0 60 60"><rect x="8" y="16" width="44" height="24" rx="2" fill="#4a4f55"/><rect x="8" y="42" width="44" height="4" fill="#4a4f55"/><rect x="8" y="48" width="44" height="4" fill="#4a4f55"/><circle cx="30" cy="28" r="7" fill="#fff"/><text x="30" y="32" font-size="11" font-weight="700" text-anchor="middle" fill="#4a4f55" font-family="Open Sans,sans-serif">$</text></svg></div>
      <h3>COURSE PRPCESS</h3>
      <p>Doloremque laudantium, totam rem aperiam, eaque ipsa quae ab illo inventore</p>
    </div>
    <div class="feature">
      <div class="feature-icon"><div class="card tilt"></div><div class="card"></div>
        <svg width="60" height="60" viewBox="0 0 60 60" fill="none" stroke="#4a4f55" stroke-width="3"><circle cx="30" cy="30" r="14"/><path d="M12 32v-4a18 18 0 0 1 36 0v4"/><rect x="8" y="28" width="7" height="12" fill="#4a4f55"/><rect x="45" y="28" width="7" height="12" fill="#4a4f55"/><path d="M48 40q0 10-12 10h-4"/></svg></div>
      <h3>GOOD SUPPORTS</h3>
      <p>Doloremque laudantium, totam rem aperiam, eaque ipsa quae ab illo inventore</p>
    </div>
    <div class="feature">
      <div class="feature-icon"><div class="card tilt"></div><div class="card"></div>
        <svg width="60" height="60" viewBox="0 0 60 60" fill="#4a4f55"><circle cx="30" cy="12" r="5"/><rect x="24" y="19" width="12" height="12" rx="2"/><path d="M18 32h24l-4 22H22z"/></svg></div>
      <h3>TRAINED FACILITY</h3>
      <p>Doloremque laudantium, totam rem aperiam, eaque ipsa quae ab illo inventore</p>
    </div>
  </div>
</section>

<section class="band courses">
  <h2 class="section-title">OUR FEATURED COURSES</h2>
  <div class="course-grid">
    <article class="course-card">
      <div class="course-photo" role="img" aria-label="Photo of business people working at a glass meeting table" style="background:linear-gradient(160deg,#dfe6ea,#9aa7b0 60%,#5d6872)"></div>
      <h3 class="highlight">LOREM ISPUM DOLAR</h3>
      <p>Lorem ipsum dolor sit ameetudip iscing elitrutrumunc liberocidunt</p>
      <div class="course-meta"><span class="stars">★★★★☆</span><span class="price">190$ <s>290$</s></span><span class="seats">15 <svg width="9" height="10" viewBox="0 0 9 10"><circle cx="4.5" cy="2.5" r="2.5" fill="#333a40"/><path d="M0 10a4.5 4 0 0 1 9 0z" fill="#333a40"/></svg></span></div>
    </article>
    <article class="course-card">
      <div class="course-photo" role="img" aria-label="Photo of colleagues talking across a boardroom table" style="background:linear-gradient(160deg,#6b6d70,#3e4044 60%,#24262a)"></div>
      <h3>LOREM ISPUM DOLAR</h3>
      <p>Lorem ipsum dolor sit ameetudip iscing elitrutrumunc liberocidunt</p>
      <div class="course-meta"><span class="stars">★★★★☆</span><span class="price">190$ <s>290$</s></span><span class="seats">15 <svg width="9" height="10" viewBox="0 0 9 10"><circle cx="4.5" cy="2.5" r="2.5" fill="#333a40"/><path d="M0 10a4.5 4 0 0 1 9 0z" fill="#333a40"/></svg></span></div>
    </article>
    <article class="course-card">
      <div class="course-photo" role="img" aria-label="Photo of a presenter leading a meeting in a bright office" style="background:linear-gradient(160deg,#f1f2f0,#b8bdb9 55%,#6e7570)"></div>
      <h3>LOREM ISPUM DOLAR</h3>
      <p>Lorem ipsum dolor sit ameetudip iscing elitrutrumunc liberocidunt</p>
      <div class="course-meta"><span class="stars">★★★★☆</span><span class="price">190$ <s>290$</s></span><span class="seats">15 <svg width="9" height="10" viewBox="0 0 9 10"><circle cx="4.5" cy="2.5" r="2.5" fill="#333a40"/><path d="M0 10a4.5 4 0 0 1 9 0z" fill="#333a40"/></svg></span></div>
    </article>
    <article class="course-card">
      <div class="course-photo" role="img" aria-label="Photo of a group of business people standing together" style="background:linear-gradient(160deg,#8a5a46,#5a4a48 50%,#2e2f35)"></div>
      <h3>LOREM ISPUM DOLAR</h3>
      <p>Lorem ipsum dolor sit ameetudip iscing elitrutrumunc liberocidunt</p>
      <div class="course-meta"><span class="stars">★★★★☆</span><span class="price">190$ <s>290$</s></span><span class="seats">15 <svg width="9" height="10" viewBox="0 0 9 10"><circle cx="4.5" cy="2.5" r="2.5" fill="#333a40"/><path d="M0 10a4.5 4 0 0 1 9 0z" fill="#333a40"/></svg></span></div>
    </article>
  </div>
</section>

<section class="band news">
  <h2 class="section-title">LATEST NEWS</h2>
  <div class="news-grid">
    <article class="news-card">
      <div class="news-photo" role="img" aria-label="Photo of a team gathered around a laptop" style="background:linear-gradient(160deg,#d9d4cf,#8d857e 60%,#4f4a47)"></div>
      <div class="news-body"><h3 class="highlight">LOREM IPSUM DOLOR SIT</h3><p>Praesent quis sem ac eros porttitor Class aptentsociosqu ad litora torque per conubia nostra, per inceptuis vitae</p><div class="btn-more">READ MORE</div></div>
    </article>
    <article class="news-card">
      <div class="news-photo" role="img" aria-label="Photo of business people shaking hands" style="background:linear-gradient(160deg,#f4f4f4,#b9bcc0 55%,#4a4d52)"></div>
      <div class="news-body"><h3>LOREM IPSUM DOLOR SIT</h3><p>Praesent quis sem ac eros porttitorcf Class aptentsociosqu ad litora torque per conubia nostra, per inceptuis vita</p><div class="btn-more">READ MORE</div></div>
    </article>
    <article class="news-card">
      <div class="news-photo" role="img" aria-label="Photo of a cheerful team giving thumbs up" style="background:linear-gradient(160deg,#eef0f0,#bfc2c0 55%,#77797a)"></div>
      <div class="news-body"><h3>LOREM IPSUM DOLOR SIT</h3><p>Praesent quis sem ac eros porttitofcg Class aptentsociosqu ad litora torque per conubia nostra, per inceptuis vita</p><div class="btn-more">READ MORE</div></div>
    </article>
    <article class="news-card">
      <div class="news-photo" role="img" aria-label="Photo of colleagues greeting each other with a handshake" style="background:linear-gradient(160deg,#c9b08c,#7c6a5c 55%,#2f3036)"></div>
      <div class="news-body"><h3>LOREM IPSUM DOLOR SIT</h3><p>Praesent quis sem ac eros porttitor vcfg. Class aptentsociosqu ad litora torquent per conubia nostra, per inceptuis vitae</p><div class="btn-more">READ MORE</div></div>
    </article>
  </div>
</section>

<section class="band events">
  <h2 class="section-title">LATEST EVENTS</h2>
  <div class="event-grid">
    <article class="event">
      <div class="event-photo" role="img" aria-label="Photo of a team reviewing work on a laptop" style="background:linear-gradient(160deg,#d8dde4,#7d8796 55%,#33394a)"></div>
      <div class="event-info"><div class="date"><b>02</b><span>Mar</span></div><p>Lorem ipsum dolor sit amet, consect etur adipiscing eli</p></div>
    </article>
    <article class="event">
      <div class="event-photo" role="img" aria-label="Photo of hands working with a tablet and notebook" style="background:linear-gradient(160deg,#f3f5f7,#c3ccd4 55%,#6f8aa6)"></div>
      <div class="event-info"><div class="date"><b>15</b><span>Mar</span></div><p>Lorem ipsum dolor sit amet consecte tur adipiscing eli</p></div>
    </article>
    <article class="event">
      <div class="event-photo" role="img" aria-label="Photo of people reviewing paperwork on a desk" style="background:linear-gradient(160deg,#f6f6f6,#c7c9cc 50%,#3d4350)"></div>
      <div class="event-info"><div class="date"><b>20</b><span>Mar</span></div><p>Lorem ipsum dolor sit amet consecte tur adipiscing eli</p></div>
    </article>
  </div>
</section>

<footer class="band site-footer">
  <nav class="footer-nav"><span>Home</span><i>/</i><span>About</span><i>/</i><span>Course</span><i>/</i><span>Events</span><i>/</i><span>Events</span><i>/</i><span>Gallery</span><i>/</i><span>Blog</span><i>/</i><span>Contact us</span></nav>
  <p class="copyright">Copyright 2016. <b>The Harbor Loft.</b> All rights Resverd</p>
  <div class="social"><span></span><span></span><span></span><span></span><span></span></div>
</footer>

</body>
</html>
```